Email Signatures

I would like to create a new email signature for my team. The design will be the same for everyone, with only individual details such as name and email changing. You can also see our brand style on our website. https://www.tlmbespokehomes.com.au/

Target Market(s)

Clients for new builds or renovations

Industry/Entity Type

Construction

Colors

Designer to choose colors to be used in the design.

```html
<!DOCTYPE html>
<html lang="en">
<head>
<meta charset="utf-8">
<title>TLM Bespoke Homes – Email Signature</title>
<link href="https://fonts.googleapis.com/css2?family=Exo+2:ital,wght@1,800&family=Poppins:wght@400;500;600;700&display=swap" rel="stylesheet">
<style>
  :root {
    --green: #1f9a3a;
    --green-dark: #17662a;
    --green-bright: #3bb54a;
    --black: #0c0c0c;
    --ink: #1a1a1a;
    --logo-ink: #2b2b2b;
    --white: #ffffff;
    --backdrop: #f2f2f2;
    --photo-light: #8a7f78;
    --photo-dark: #2a2526;
  }
  * { box-sizing: border-box; margin: 0; padding: 0; }
  html, body {
    width: 1200px; height: 366px; overflow: hidden;
    background: var(--backdrop);
    font-family: "Poppins", sans-serif;
  }
  .signature {
    position: absolute; left: 72px; top: 62px;
    width: 1058px; height: 244px;
    background: var(--white);
    overflow: hidden;
  }
  .shapes { position: absolute; inset: 0; }
  .brand-banner {
    position: absolute; left: 520px; top: 10px; width: 520px;
    text-align: center;
    font-family: "Exo 2", sans-serif; font-style: italic; font-weight: 800;
    font-size: 31px; letter-spacing: 1px; color: var(--white);
    text-transform: uppercase;
  }
  .wordmark {
    position: absolute; left: 40px; top: 62px;
    display: flex; align-items: center; gap: 14px;
  }
  .wordmark-square { width: 22px; height: 22px; background: var(--green); }
  .wordmark-name {
    font-weight: 700; font-size: 92px; line-height: 1;
    letter-spacing: 4px; color: var(--logo-ink);
  }
  .person { position: absolute; left: 526px; top: 80px; }
  .person-name {
    font-weight: 600; font-size: 42px; line-height: 1; color: var(--ink);
  }
  .person-name .first { color: var(--green); }
  .person-role {
    margin-top: 10px; font-weight: 500; font-size: 19px; line-height: 1; color: var(--ink);
  }
  .person-blurb {
    margin-top: 9px; font-size: 12px; line-height: 1; color: var(--ink);
  }
  .contact-bar {
    position: absolute; top: 196px; height: 22px;
    display: flex; align-items: center; gap: 8px;
    font-size: 13.5px; font-weight: 500; color: var(--white);
  }
  .contact-label { font-weight: 700; font-size: 15px; color: var(--green-bright); margin-right: 6px; }
  .contact-icon { width: 18px; height: 18px; flex: none; }
  .contact-left { left: 24px; }
  .contact-right { left: 532px; gap: 6px; }
  .contact-right .spacer { width: 10px; }
</style>
</head>
<body>
  <div class="signature">
    <svg class="shapes" width="1058" height="244" viewBox="0 0 1058 244" aria-hidden="true">
      <defs>
        <linearGradient id="bannerGreen" x1="0" y1="0" x2="1" y2="0">
          <stop offset="0" stop-color="#15602a"/>
          <stop offset="0.5" stop-color="#1e8a35"/>
          <stop offset="1" stop-color="#17662a"/>
        </linearGradient>
        <linearGradient id="photoTone" x1="0" y1="0" x2="0" y2="1">
          <stop offset="0" stop-color="var(--photo-light)"/>
          <stop offset="1" stop-color="var(--photo-dark)"/>
        </linearGradient>
      </defs>
      <!-- top brand band -->
      <polygon points="420,0 1058,0 1058,58 516,58" fill="url(#bannerGreen)"/>
      <polygon points="836,58 1058,58 1058,77 860,77" fill="var(--black)"/>
      <!-- contact band -->
      <rect x="0" y="186" width="1058" height="38" fill="var(--black)"/>
      <!-- bottom stripes -->
      <polygon points="0,236 396,236 390,244 0,244" fill="var(--green)"/>
      <polygon points="404,234 1058,234 1058,244 396,244" fill="var(--black)"/>
      <!-- portrait hexagon -->
      <polygon points="412,9 506,62 506,169 412,222 320,169 320,62" fill="var(--white)" stroke="var(--green)" stroke-width="3"/>
      <polygon points="412,16 500,66 500,166 412,216 326,166 326,66" fill="url(#photoTone)" role="img" aria-label="Portrait photo of the team member"/>
    </svg>

    <div class="brand-banner">TLM Bespoke Homes</div>

    <div class="wordmark">
      <span class="wordmark-square"></span>
      <span class="wordmark-name">TLM</span>
    </div>

    <div class="person">
      <div class="person-name"><span class="first">Daniel</span> Hayes</div>
      <div class="person-role">Manager</div>
      <div class="person-blurb">Lorem Ipsum is simply dummy text of the printing &nbsp;&amp; typesetting industry.</div>
    </div>

    <div class="contact-bar contact-left">
      <span class="contact-label">CONTACT US</span>
      <svg class="contact-icon" viewBox="0 0 18 18" aria-hidden="true">
        <circle cx="9" cy="9" r="9" fill="var(--green)"/>
        <path d="M6 4.5 L7.6 4.5 L8.3 6.8 L7.3 7.6 C7.9 8.9 9 10 10.4 10.7 L11.2 9.7 L13.5 10.4 L13.5 12 C13.5 12.8 12.9 13.4 12 13.3 C8.3 12.9 5.1 9.7 4.7 6 C4.6 5.1 5.2 4.5 6 4.5 Z" fill="var(--white)"/>
      </svg>
      <span>+61 400 123 456</span>
    </div>

    <div class="contact-bar contact-right">
      <svg class="contact-icon" viewBox="0 0 18 18" aria-hidden="true">
        <circle cx="9" cy="9" r="9" fill="var(--green)"/>
        <rect x="4.5" y="6" width="9" height="6.5" rx="0.8" fill="var(--white)"/>
        <path d="M4.8 6.4 L9 9.6 L13.2 6.4" fill="none" stroke="var(--green)" stroke-width="1"/>
      </svg>
      <span>info@tlmbespokehomes.com.au</span>
      <span class="spacer"></span>
      <svg class="contact-icon" viewBox="0 0 18 18" aria-hidden="true">
        <circle cx="9" cy="9" r="9" fill="var(--green)"/>
        <circle cx="9" cy="9" r="4.6" fill="none" stroke="var(--white)" stroke-width="1.2"/>
        <path d="M4.4 9 H13.6 M9 4.4 C6.8 7 6.8 11 9 13.6 M9 4.4 C11.2 7 11.2 11 9 13.6" fill="none" stroke="var(--white)" stroke-width="1"/>
      </svg>
      <span>tlmbespokehomes.com.au</span>
    </div>
  </div>
</body>
</html>
```